Need Business cards

Im a new realtor and already have a logo. I would like to purchase a Business card design that catches customer's attention, its creative, and modern.

Marisol Quintero
Realtor ®
(555) 318 4027
marisolqtrhomes@brindlemail.com

Target Market(s)

investors, buyers and seller, property management

Industry/Entity Type

real estate,

Contact Information for Business Card

Marisol Quintero

Requirements
Must have
• BOTH LOGOS, WOULD LIKE TO SEE WITH DIFFERENT OPTIONS WITH EITHER PICTURE

```html
<!DOCTYPE html>
<html lang="en">
<head>
<meta charset="utf-8">
<title>Marisol Quintero – Realtor Business Card</title>
<link href="https://fonts.googleapis.com/css2?family=Montserrat:wght@400;500;600;700&display=swap" rel="stylesheet">
<style>
  :root {
    --page-bg: #e9e6e1;
    --card-black: #1c1c1c;
    --gold: #d4ad3c;
    --gold-light: #f0d36a;
    --gold-dark: #b28a22;
    --ink: #1b1b1b;
    --marble: #f1f1f1;
    --strip: #f7f7f8;
    --brand-blue: #2b5aa8;
    --photo-light: #efefef;
    --photo-warm: #d9c3a6;
    --photo-dark: #2a2624;
  }
  * { margin: 0; padding: 0; box-sizing: border-box; }
  html, body { width: 900px; height: 1200px; overflow: hidden; }
  body {
    background: var(--page-bg);
    font-family: "Montserrat", Arial, sans-serif;
    position: relative;
  }
  .card {
    position: absolute;
    left: 73px;
    width: 773px;
    height: 448px;
    border-radius: 22px;
    overflow: hidden;
  }
  /* Front */
  .card-front {
    top: 135px;
    background: var(--card-black);
    box-shadow: 0 10px 24px rgba(0,0,0,.25);
  }
  .monogram {
    position: absolute;
    left: 0; right: 0; top: 90px; height: 200px;
    display: flex; justify-content: center; align-items: center; gap: 16px;
  }
  .monogram-square { width: 20px; height: 20px; background: var(--gold); }
  .monogram-text {
    font-size: 72px; font-weight: 500; letter-spacing: 8px;
    color: var(--gold);
  }
  .front-name {
    position: absolute; left: 0; right: 0; top: 313px;
    text-align: center;
    font-size: 27px; font-weight: 600; letter-spacing: .5px;
    color: var(--gold);
  }
  .front-title {
    position: absolute; left: 0; right: 0; top: 349px;
    display: flex; justify-content: center; align-items: center; gap: 10px;
    font-size: 18px; font-weight: 500; letter-spacing: 1px;
    color: var(--gold);
  }
  .front-title .rule { width: 80px; height: 1.5px; background: var(--gold); }
  /* Back */
  .card-back {
    top: 625px;
    background:
      linear-gradient(120deg, transparent 40%, rgba(200,200,200,.35) 41%, transparent 43%),
      linear-gradient(70deg, transparent 62%, rgba(190,190,190,.3) 63%, transparent 65%),
      linear-gradient(160deg, #fafafa, var(--marble) 55%, #e8e8e8);
    box-shadow: 0 10px 24px rgba(0,0,0,.2);
  }
  .portrait {
    position: absolute; left: 0; top: 0; width: 410px; height: 424px;
    background:
      radial-gradient(ellipse 190px 260px at 205px 230px, rgba(217,195,166,.85), rgba(217,195,166,0) 100%),
      linear-gradient(180deg, var(--photo-light) 0%, var(--photo-light) 45%, #8a7d70 80%, var(--photo-dark) 100%);
    -webkit-mask-image: linear-gradient(90deg, #000 88%, transparent 100%);
            mask-image: linear-gradient(90deg, #000 88%, transparent 100%);
  }
  .agent-name {
    position: absolute; left: 406px; right: 0; top: 86px;
    text-align: center; font-size: 30px; font-weight: 700; color: var(--ink);
  }
  .agent-title {
    position: absolute; left: 406px; right: 0; top: 126px;
    text-align: center; font-size: 27px; font-weight: 400; color: var(--ink);
  }
  .contact-divider {
    position: absolute; left: 432px; top: 190px; width: 296px; height: 36px;
  }
  .contact-line {
    position: absolute; left: 406px; right: 0;
    text-align: center; font-size: 20px; color: var(--ink);
  }
  .contact-phone { top: 258px; }
  .contact-email { top: 293px; font-size: 19px; }
  .brokerage-strip {
    position: absolute; left: 406px; right: 0; top: 357px; height: 67px;
    background: var(--strip);
    display: flex; justify-content: center; align-items: center;
  }
  .brokerage-name {
    font-size: 24px; font-weight: 700; letter-spacing: 1px;
    color: var(--brand-blue);
  }
  .gold-band {
    position: absolute; left: 0; right: 0; bottom: 0; height: 24px;
    background: linear-gradient(90deg, var(--gold-dark), var(--gold-light) 45%, var(--gold) 70%, var(--gold-dark));
  }
</style>
</head>
<body>
  <section class="card card-front">
    <div class="monogram">
      <span class="monogram-text">MQ</span>
      <span class="monogram-square"></span>
    </div>
    <div class="front-name">MARISOL QUINTERO</div>
    <div class="front-title"><span class="rule"></span>REALTOR<span class="rule"></span></div>
  </section>

  <section class="card card-back">
    <div class="portrait" role="img" aria-label="Portrait photo of the realtor in a black top against a light backdrop"></div>
    <div class="agent-name">Marisol Quintero</div>
    <div class="agent-title">Realtor ®</div>
    <svg class="contact-divider" viewBox="0 0 296 36" aria-hidden="true">
      <line x1="0" y1="18" x2="90" y2="18" stroke="#1b1b1b" stroke-width="2"/>
      <line x1="206" y1="18" x2="296" y2="18" stroke="#1b1b1b" stroke-width="2"/>
      <circle cx="119" cy="18" r="17" fill="#1b1b1b"/>
      <path d="M112 10 l4 -1 l3 6 l-2.5 2 a11 11 0 0 0 5 5 l2 -2.5 l6 3 l-1 4 a3 3 0 0 1 -3 1.5 a20 20 0 0 1 -15 -15 a3 3 0 0 1 1.5 -3z" fill="#fff"/>
      <circle cx="171" cy="18" r="17" fill="#1b1b1b"/>
      <rect x="161" y="11" width="20" height="14" rx="2" fill="#fff"/>
      <path d="M161.5 12 l9.5 7.5 l9.5 -7.5" fill="none" stroke="#1b1b1b" stroke-width="1.8"/>
    </svg>
    <div class="contact-line contact-phone">(555) 318 4027</div>
    <div class="contact-line contact-email">marisolqtrhomes@brindlemail.com</div>
    <div class="brokerage-strip"><span class="brokerage-name">NORTHVALE REALTY</span></div>
    <div class="gold-band"></div>
  </section>
</body>
</html>
```